Real Estate Renovation and Rental:Business Card/Logo Design Project

Corliss Grove LLC is a small partnership that buys homes to renovate, then provide as rentals to people who may not currently be able to purchase a home - but we also coach them on how to improve their credit so that, in 2-5 years, they may be able to buy a home. Maybe even the one they're living in.

We are based in Sonoma County of Northern California, operating in communities including Healdsburg, Windsor, Santa Rosa, and Cloverdale.

Please design a business card, but the same logo should work for signs that we will post on the homes as they are being renovated.

The design should be clean, contemporary, professional but warm. I'd love to see a rooftop feature, or some other element of a house. Again, not too much detail, clean and welcoming. The design must include "Corliss Grove LLC" - but "CGLLC" could also be used as a primary name, with "Corliss Grove LLC" in smaller print somewhere. If using "CGLLC", the CG could be visually distinct (larger, different color, font) than the LLC part of the name but they must be together.
Updates

just conferring with partner to choose a final design ... should be ready to choose soon and will post

Industry/Entity Type

Business

Requirements
Must have
• the name "Corliss Grove LLC"
for business card design, and leave room for us to customize with partner names, address, telephone numbers, email addresses
Nice to have
• some element of a house included

```html
<!DOCTYPE html>
<html lang="en">
<head>
<meta charset="utf-8">
<title>Corliss Grove LLC – Business Card</title>
<link rel="stylesheet" href="https://fonts.googleapis.com/css2?family=Arimo:wght@400;700&display=swap">
<style>
  :root {
    --backdrop: #2b2b2b;
    --card-white: #f4f4f4;
    --brand-blue: #1f74bb;
    --ink-grey: #4a4a4a;
    --ink-white: #ffffff;
  }
  * { box-sizing: border-box; margin: 0; padding: 0; }
  html, body {
    width: 1200px; height: 900px; overflow: hidden;
    background: var(--backdrop);
    font-family: "Arimo", Arial, sans-serif;
  }
  .canvas { position: relative; width: 1200px; height: 900px; }

  .card {
    position: absolute;
    width: 560px; height: 320px;
    box-shadow: 0 10px 30px rgba(0,0,0,.45);
  }

  /* Front: contact side */
  .card-front {
    left: 90px; top: 110px;
    background: var(--card-white);
    color: var(--ink-grey);
  }
  .front-wordmark {
    position: absolute; right: 40px; top: 42px;
    font-weight: 700; font-size: 22px; letter-spacing: 1px;
    color: var(--brand-blue);
    white-space: nowrap;
  }
  .contact { position: absolute; left: 40px; top: 120px; font-size: 13px; line-height: 1.35; white-space: nowrap; }
  .contact-name { font-weight: 700; font-size: 20px; color: var(--brand-blue); line-height: 1.1; }
  .contact-title { margin-bottom: 14px; }
  .contact-address { margin-bottom: 14px; }
  .label { color: var(--brand-blue); }
  .strong { font-weight: 700; }
  .strong-blue { font-weight: 700; color: var(--brand-blue); }

  /* Back: brand side */
  .card-back {
    left: 550px; top: 470px;
    background: var(--brand-blue);
    color: var(--ink-white);
    display: flex; flex-direction: column; align-items: center; justify-content: center;
    padding: 0 30px;
  }
  .back-wordmark {
    font-weight: 700; font-size: 38px; letter-spacing: 1px;
    white-space: nowrap;
    padding: 14px 8px;
    border-top: 1.5px solid var(--ink-white);
    border-bottom: 1.5px solid var(--ink-white);
  }
  .back-url { margin-top: 36px; font-size: 15px; letter-spacing: .5px; white-space: nowrap; }
</style>
</head>
<body>
<main class="canvas">
  <section class="card card-front" aria-label="Business card, contact side">
    <div class="front-wordmark">CORLISS GROVE LLC</div>
    <div class="contact">
      <p class="contact-name">Desmond Hale</p>
      <p class="contact-title">Manager/Director</p>
      <p class="contact-address">
        CorlissGroveLLC.com<br>
        Po Box 0487219<br>
        Riverton City Central, 348102
      </p>
      <p><span class="label">phone:</span> 0415 382 640</p>
      <p><span class="label">email:</span> <span class="strong">Desmond</span>@CorlissGroveLLC.com</p>
      <p>www.<span class="strong-blue">CorlissGroveLLC</span>.com</p>
    </div>
  </section>

  <section class="card card-back" aria-label="Business card, brand side">
    <div class="back-wordmark">CORLISS GROVE LLC</div>
    <p class="back-url">www.CorlissGroveLLC.com</p>
  </section>
</main>
</body>
</html>
```